lark to lead - dorian whitcombe personal speaking/consulting website

custom website for my personal speaking/consulting services brand, you can see the basic site we are using as a placeholder at www.larktolead.example now. I want to re-position this to more of a personal brand site and have video samples of speaking events, downloadable content, a video blog, and links to podcast. I really like the design of marcoveldin.example and the feature set should be fairly similar to his. I'll begin to compile more stock images etc. to use for sliders like he has done, for now we'll need to use stock imagery or existing photography from my social accounts. You can get a feel for social at all platforms/dwhitrealty i.e. facebook.com/dwhitrealty. the site should be primarily geared toward showcasing speaking/consulting services and content, as well as be flexible to allow for additional downloadables etc. in the future.

Target Market(s)

entrepreneurs and leaders looking to grow themselves, their business, and those they lead.

Coding

Coded - Design and coding required

Number of Pages Required

3 page

Font styles to use
Sans Serif

Colors

Designer to choose colors to be used in the design.

Requirements
Must have
• modern slick design, video blog, podcast feed, registration for people to subscribe to newsletter

```html
<!DOCTYPE html>
<html lang="en">
<head>
<meta charset="utf-8">
<title>Lark to Lead</title>
<link href="https://fonts.googleapis.com/css2?family=Bangers&family=Raleway:wght@400;500;600&display=swap" rel="stylesheet">
<style>
:root{
  --navy:#1b3272;
  --ink:#111111;
  --white:#ffffff;
  --footer:#1f1f1f;
  --text:#444444;
  --line:#8c8c8c;
}
*{box-sizing:border-box;margin:0;padding:0}
html,body{width:1200px;height:3838px;overflow:hidden;background:var(--white)}
body{position:relative;font-family:'Raleway',sans-serif;color:var(--text)}
.abs{position:absolute}
.display{font-family:'Bangers',sans-serif;letter-spacing:1px;font-weight:400}
.btn{position:absolute;display:flex;align-items:center;justify-content:center;font-size:12px;color:var(--white);background:var(--navy)}

/* hero */
.hero{left:0;top:0;width:1200px;height:629px;background:linear-gradient(100deg,#2a3f86 0%,#3a4f8e 35%,#6c5b7a 60%,#3b4c83 100%);overflow:hidden}
.hero-photo{left:0;top:0;width:1200px;height:629px;background:radial-gradient(ellipse at 25% 45%,rgba(30,50,120,.9),rgba(60,80,140,.3) 60%,rgba(120,90,110,.2))}
.brand{left:146px;top:34px;font-size:46px;color:var(--white)}
.nav{left:493px;top:52px;display:flex;font-size:12px;color:var(--white)}
.nav span{margin-right:54px}
.hero-title{left:480px;top:210px;width:600px;text-align:center;font-size:86px;color:var(--white)}
.hero-copy{left:530px;top:322px;width:500px;text-align:center;font-size:12px;line-height:24px;color:var(--white)}
.hero-btn{left:724px;top:435px;width:112px;height:41px;border:1px solid rgba(255,255,255,.7)}
.notch{left:500px;top:596px}

/* about */
.about-photo{left:142px;top:683px;width:390px;height:423px;background:linear-gradient(160deg,#5a5a5a,#1f1f1f)}
.about-frame{left:157px;top:698px;width:362px;height:393px;border:3px solid var(--white)}
.about-title{left:560px;top:712px;font-size:74px;color:var(--ink)}
.about-title em{font-style:normal;color:var(--navy)}
.about-copy{left:560px;top:830px;width:482px;font-size:12px;line-height:24px}
.about-btn{left:560px;top:1030px;width:111px;height:40px}

/* inspiring */
.inspire{left:0;top:1167px;width:601px;height:517px;background:var(--navy)}
.inspire-divider{left:601px;top:1167px;width:10px;height:517px;background:#0d1633}
.inspire-photo{left:611px;top:1167px;width:589px;height:517px;background:linear-gradient(120deg,#8a8f8a,#c8b59a 45%,#6d6a62)}
.inspire-title{left:130px;top:1235px;width:490px;text-align:right;font-size:56px;line-height:66px;color:var(--white);transform:rotate(-5deg);transform-origin:right center}
.inspire-copy{left:150px;top:1428px;width:422px;text-align:right;font-size:12px;line-height:24px;color:var(--white)}
.inspire-btn{left:453px;top:1585px;width:113px;height:41px;border:1px solid var(--white);background:transparent}

/* video */
.video{left:107px;top:1723px;width:984px;height:544px;background:linear-gradient(180deg,#7fb0d6 0%,#6d9ec6 55%,#4c4c4c 80%,#6a3a2e 100%)}
.play{left:526px;top:1953px;width:150px;height:90px;background:rgba(20,20,20,.85);border-radius:12px}

/* tiles */
.tile-a{left:142px;top:2309px;width:444px;height:322px;background:linear-gradient(135deg,#6da5c6,#2d3b48 60%,#1e2a33)}
.tile-b{left:611px;top:2348px;width:444px;height:320px;background:linear-gradient(180deg,#3a1d6a,#1b1840 50%,#2b3b3a)}
.tile-label{position:absolute;display:flex;align-items:center;justify-content:center;width:155px;height:50px;background:var(--navy);border:1px solid var(--white);color:var(--white);font-size:16px}

/* featured */
.featured-title{left:0;top:2760px;width:1200px;text-align:center;font-size:56px;color:var(--ink)}
.member{position:absolute;width:299px}
.member-photo{width:100%}
.member-name{height:48px;background:var(--navy);color:var(--white);display:flex;align-items:center;justify-content:center;font-family:'Bangers',sans-serif;font-size:24px;letter-spacing:1px;border:1px solid #0c1a45}

/* newsletter */
.newsletter{left:0;top:3350px;width:1200px;height:161px;background:var(--navy)}
.news-title{left:150px;top:3380px;width:325px;text-align:center;font-size:38px;line-height:44px;color:var(--white)}
.news-input{left:510px;top:3400px;width:323px;height:64px;background:var(--white);font-size:11px;color:#aaa;padding:0 24px;display:flex;align-items:center}
.news-btn{left:847px;top:3400px;width:149px;height:64px;background:#000;color:var(--white);font-size:20px;font-weight:600;display:flex;align-items:center;justify-content:center}

/* footer */
.footer{left:0;top:3511px;width:1200px;height:327px;background:var(--footer)}
.footer-brand{left:0;top:3570px;width:1200px;text-align:center;font-size:62px;color:var(--white)}
.socials{left:480px;top:3667px;display:flex;gap:16px}
.socials span{width:36px;height:36px;border:1.5px solid var(--white);border-radius:50%}
.footer-rule{left:142px;top:3752px;width:915px;height:1px;background:var(--line)}
.copyright{left:0;top:3786px;width:1200px;text-align:center;font-size:11px;color:var(--white)}
</style>
</head>
<body>

<header class="abs hero">
  <div class="abs hero-photo" role="img" aria-label="Speaker in a blue suit addressing a blurred audience"></div>
  <div class="abs brand display">LARK TO LEAD</div>
  <nav class="abs nav"><span>Home</span><span>About Us</span><span>Podcast</span><span>Resources</span><span>Contact Us</span>
    <svg width="16" height="16" viewBox="0 0 16 16" fill="none" stroke="#fff" stroke-width="1.4"><circle cx="7" cy="7" r="5"/><line x1="10.6" y1="10.6" x2="14.5" y2="14.5"/></svg>
  </nav>
  <h1 class="abs hero-title display">LARK TO LEAD</h1>
  <p class="abs hero-copy">Lorem Ipsum is simply dummy text of the printing and typesetting industry. Lorem Ipsum has been the industry's standard dummy text ever since the 1500s, when an unknown printer took a galley of type and scrambled</p>
  <div class="btn hero-btn">Read More</div>
  <svg class="abs notch" width="200" height="33" viewBox="0 0 200 33"><path d="M0 33 C60 33 60 2 100 2 C140 2 140 33 200 33 Z" fill="#fff"/><polyline points="93,20 100,26 107,20" fill="none" stroke="#1b3272" stroke-width="2"/></svg>
</header>

<section>
  <div class="abs about-photo" role="img" aria-label="Portrait of Dorian Whitcombe in a dark suit and red tie"></div>
  <div class="abs about-frame"></div>
  <h2 class="abs about-title display">ABOUT <em>LARK</em></h2>
  <p class="abs about-copy">Lorem Ipsum is simply dummy text of the printing and typesetting industry. Lorem Ipsum has been the industry's standard dummy text ever since the 1500s, when an unknown printer took a galley of type and scrambled it to make a type specimen book. It has survived not only five centuries, but also the leap into electronic typesetting, remaining essentially unchanged. It was popularised in the 1960s with the release of Letraset sheets containing Lorem Ipsum passages, and more recently with desktop publishing software like Aldus PageMaker including versions of Lorem Ipsum.</p>
  <div class="btn about-btn">Read More</div>
</section>

<section>
  <div class="abs inspire"></div>
  <div class="abs inspire-divider"></div>
  <div class="abs inspire-photo" role="img" aria-label="Selfie of Dorian Whitcombe and a companion on a flight"></div>
  <h2 class="abs inspire-title display">INSPIRING LIFE<br>WITH DORIAN WHITCOMBE</h2>
  <p class="abs inspire-copy">Lorem Ipsum is simply dummy text of the printing and typesetting industry. Lorem Ipsum has been the industry's standard dummy text ever since the 1500s, when an unknown printer took a galley of type and scrambled it to make a type specimen book. It has survived not only five centuries, but also the leap into electronic</p>
  <div class="btn inspire-btn">Read More</div>
</section>

<section>
  <div class="abs video" role="img" aria-label="Video still of Dorian Whitcombe speaking in a television studio"></div>
  <div class="abs play"></div>
  <svg class="abs" style="left:583px;top:1978px" width="40" height="40" viewBox="0 0 40 40"><polygon points="4,2 38,20 4,38" fill="#fff"/></svg>
</section>

<section>
  <div class="abs tile-a" role="img" aria-label="Dorian Whitcombe seated at a studio desk"></div>
  <div class="tile-label" style="left:286px;top:2445px">Podcast</div>
  <div class="abs tile-b" role="img" aria-label="Dorian Whitcombe with a guest at an evening event"></div>
  <div class="tile-label" style="left:756px;top:2482px">Events</div>
</section>

<section>
  <h2 class="abs featured-title display">FEATURED PODCAST</h2>
  <div class="member" style="left:0;top:2911px"><div class="member-photo" style="height:339px;background:linear-gradient(180deg,#eef0f2,#c9cdd3)" role="img" aria-label="Podcast guest portrait"></div><div class="member-name">NAME HERE</div></div>
  <div class="member" style="left:301px;top:2883px"><div class="member-photo" style="height:337px;background:linear-gradient(180deg,#e8ece6,#b9c7a7)" role="img" aria-label="Podcast guest portrait"></div><div class="member-name">NAME HERE</div></div>
  <div class="member" style="left:601px;top:2911px"><div class="member-photo" style="height:339px;background:linear-gradient(180deg,#b6c9d6,#5d6f7e)" role="img" aria-label="Podcast guest portrait"></div><div class="member-name">NAME HERE</div></div>
  <div class="member" style="left:901px;top:2883px"><div class="member-photo" style="height:337px;background:linear-gradient(180deg,#f0eeec,#d6cfc8)" role="img" aria-label="Podcast guest portrait"></div><div class="member-name">NAME HERE</div></div>
</section>

<section>
  <div class="abs newsletter"></div>
  <h2 class="abs news-title display">SUBSCRIBE TO OUR<br>NEWSLETTER</h2>
  <div class="abs news-input">Email Address...</div>
  <div class="abs news-btn">Subscribe</div>
</section>

<footer>
  <div class="abs footer"></div>
  <div class="abs footer-brand display">LARK TO LEAD</div>
  <div class="abs socials"><span></span><span></span><span></span><span></span><span></span></div>
  <div class="abs footer-rule"></div>
  <p class="abs copyright">copyright © 2019 LARK TO LEAD</p>
</footer>

</body>
</html>
```